Symposium Flyer

I need a flyer for advertising an upcoming symposium titled, "Stirring and settling the chromatin code", I am organizing as well as a webpage design for the symposium. The Symposium is taking place on Thursday, February 7th, 2019 at the Valdmere University Harrowgate School of Medicine. It is being held by the Gene Regulation Centre at the Corvath Hall for Applied Discovery (Maplewick Auditorium and Lobby, 1275 Larkspur Terrace Way, Philadelphia, PA 19187). You can view previous symposiums from our institution at https://events.valdmere-med.example/generegulation/symposiums/

Our Keynote speakers for this symposium are:
Theodor Wallmark, M.D., Professor of Biology at the Ostrander Polytechnic Academy; Founding Member of the Brackenfield Foundation for Life Science Study; Member of the Council of Clinical Scholars.
AND
Martin (Marty) Okafor, M.D., President of the Quelvora Laboratories for Therapeutic Discovery (QLTD)

We will be adding 8 more speakers to this event, so please leave room for extra speakers to be added and for a website registration link and QR code to be added.

Please email me should have additional questions - torvik@mail.valdmere-med.example

```html
<!DOCTYPE html>
<html lang="en">
<head>
<meta charset="utf-8">
<title>Stirring and Settling the Chromatin Code — Symposium Flyer</title>
<link rel="stylesheet" href="https://fonts.googleapis.com/css2?family=Oswald:wght@700&family=Roboto+Condensed:ital,wght@0,400;0,700;1,400;1,700&display=swap">
<style>
  :root {
    --ink: #0d4a80;
    --bar: #0f4d85;
    --orange: #f0993f;
    --panel-light: #f2f8ef;
    --panel-mint: #d4ead7;
    --body: #2a2a2a;
    --black: #000;
    --white: #fff;
  }
  * { margin: 0; padding: 0; box-sizing: border-box; }
  html, body { width: 927px; height: 1200px; overflow: hidden; background: var(--black); }
  body { position: relative; font-family: "Roboto Condensed", Arial, sans-serif; color: var(--body); }

  .flyer { position: absolute; left: 78px; top: 102px; width: 771px; height: 996px; background: var(--orange); }
  .panel {
    position: absolute; left: 86px; top: 44px; width: 640px; height: 908px;
    background: radial-gradient(ellipse at 55% 45%, var(--panel-light) 0%, var(--panel-mint) 100%);
  }
  .helix-strip {
    position: absolute; left: 0; top: 0; width: 126px; height: 996px;
    background: linear-gradient(90deg, #f0993f 0%, #f3b170 40%, #f0993f 100%);
  }

  .abs { position: absolute; }
  .title {
    left: 214px; width: 580px; top: 150px; text-align: center;
    font-family: "Oswald", Impact, sans-serif; font-weight: 700; color: var(--ink);
    font-size: 44px; line-height: 50px; letter-spacing: 0.5px; text-transform: uppercase;
  }
  .host { left: 214px; width: 580px; top: 256px; text-align: center; font-size: 12px; letter-spacing: 2.4px; color: var(--body); }

  .info-bar { left: 214px; width: 580px; background: var(--bar); color: var(--white); text-align: center; font-size: 15px; line-height: 17px; }
  .info-bar b { font-weight: 700; }
  .when { top: 275px; height: 25px; padding-top: 4px; }
  .where { top: 303px; height: 40px; padding-top: 3px; }

  .section-band { left: 214px; width: 580px; height: 16px; background: var(--orange); }
  .section-label {
    left: 214px; width: 580px; text-align: center; color: var(--ink);
    font-weight: 700; font-size: 22px; letter-spacing: 9px; line-height: 22px;
  }
  .section-label span { background: transparent; }

  .keynote-name { text-align: center; color: var(--ink); font-size: 18px; font-weight: 700; line-height: 20px; }
  .keynote-role { text-align: center; color: var(--ink); font-size: 13px; font-weight: 700; font-style: italic; line-height: 16px; }
  .keynote-desc { text-align: center; font-size: 11px; line-height: 13.5px; }

  .speaker { width: 150px; text-align: center; }
  .speaker-name { color: var(--ink); font-size: 11px; font-weight: 700; line-height: 13px; }
  .speaker-role { color: var(--ink); font-size: 8px; font-style: italic; line-height: 11px; margin-top: 1px; }
  .speaker-desc { font-size: 8px; line-height: 10.5px; color: #333; }

  .footer { left: 214px; top: 965px; width: 580px; height: 89px; background: var(--bar); color: var(--white); }
  .footer-text { position: absolute; left: 12px; top: 22px; font-size: 11px; line-height: 16.5px; letter-spacing: 0.3px; }
  .footer-text b { font-weight: 700; }
  .partners { position: absolute; left: 329px; top: 7px; width: 239px; height: 75px; background: var(--white); border: 1px solid #cfd8e0; }
  .thanks { position: absolute; left: 4px; top: 7px; font-size: 8px; line-height: 10px; color: var(--bar); }
  .partner { position: absolute; display: flex; align-items: center; gap: 4px; font-size: 10px; font-weight: 700; color: var(--bar); line-height: 11px; }
  .partner i { display: block; width: 8px; height: 8px; background: var(--orange); flex: none; }
</style>
</head>
<body>
<main class="flyer-stage">
  <div class="flyer">
    <div class="panel" role="img" aria-label="Soft mint background with a faint molecular network pattern"></div>
    <div class="helix-strip" role="img" aria-label="Decorative DNA double helix running down the left edge"></div>
  </div>

  <h1 class="abs title">Stirring and settling<br>the chromatin code</h1>
  <p class="abs host">Held by the Gene Regulation Centre at the Corvath Hall</p>

  <div class="abs info-bar when"><b>WHEN:</b> Thursday, February 7th, 2019</div>
  <div class="abs info-bar where"><b>WHERE:</b> Maplewick Auditorium and Lobby, 1275 Larkspur Terrace Way,<br>Philadelphia, PA 19187</div>

  <div class="abs section-band" style="top:364px"></div>
  <div class="abs section-label" style="top:361px;">
    <span style="background:linear-gradient(var(--panel-light),var(--panel-light));padding:0 2px 0 11px;">KEYNOTE SPEAKERS</span>
  </div>

  <svg class="abs" style="left:312px;top:394px" width="124" height="130" aria-hidden="true">
    <path d="M2 78 V2 H80" fill="none" stroke="var(--orange)" stroke-width="3"/>
    <path d="M122 48 V128 H40" fill="none" stroke="var(--orange)" stroke-width="3"/>
    <rect x="8" y="6" width="110" height="118" fill="var(--white)" stroke="var(--ink)" stroke-width="1.5"/>
  </svg>
  <svg class="abs" style="left:628px;top:394px" width="124" height="130" aria-hidden="true">
    <path d="M2 78 V2 H80" fill="none" stroke="var(--orange)" stroke-width="3"/>
    <path d="M122 48 V128 H40" fill="none" stroke="var(--orange)" stroke-width="3"/>
    <rect x="8" y="6" width="110" height="118" fill="var(--white)" stroke="var(--ink)" stroke-width="1.5"/>
  </svg>

  <div class="abs" style="left:215px;width:320px;top:532px">
    <div class="keynote-name">Theodor Wallmark</div>
    <div class="keynote-role">M.D., Professor of Biology</div>
    <div class="keynote-desc">at the Ostrander Polytechnic Academy;<br>Founding Member of the Brackenfield Foundation for<br>Life Science Study; Member of the Council of Clinical Scholars.</div>
  </div>
  <div class="abs" style="left:581px;width:220px;top:532px">
    <div class="keynote-name">Martin (Marty) Okafor</div>
    <div class="keynote-role">M.D., President</div>
    <div class="keynote-desc">of the Quelvora Laboratories<br>for Therapeutic Discovery<br>(QLTD)</div>
  </div>

  <div class="abs section-band" style="top:629px"></div>
  <div class="abs section-label" style="top:626px;">
    <span style="background:linear-gradient(var(--panel-light),var(--panel-light));padding:0 2px 0 11px;">SPEAKERS</span>
  </div>

  <svg class="abs" style="left:214px;top:650px" width="580" height="260" aria-hidden="true">
    <g fill="var(--white)" stroke="var(--ink)" stroke-width="3">
      <circle cx="73" cy="52" r="44"/><circle cx="208" cy="52" r="44"/>
      <circle cx="360" cy="52" r="44"/><circle cx="512" cy="52" r="44"/>
      <circle cx="73" cy="203" r="44"/><circle cx="208" cy="203" r="44"/>
      <circle cx="360" cy="203" r="44"/><circle cx="512" cy="203" r="44"/>
    </g>
  </svg>

  <div class="abs speaker" style="left:212px;top:748px">
    <div class="speaker-name">Lena Dravik, Ph.D.</div>
    <div class="speaker-role">Assistant Professor of Cell</div>
    <div class="speaker-desc">at the Ostrander Polytechnic<br>Academy; Founding Member<br>of the Brackenfield Foundation</div>
  </div>
  <div class="abs speaker" style="left:347px;top:748px">
    <div class="speaker-name">Owen Falkner, Ph.D.</div>
    <div class="speaker-role">Assistant Professor of Genetics</div>
    <div class="speaker-desc">at the Ostrander Polytechnic<br>Academy; Founding Member<br>of the Brackenfield Foundation</div>
  </div>
  <div class="abs speaker" style="left:489px;top:748px;width:170px">
    <div class="speaker-name">Clara Hollis-Banner, Ph.D.</div>
    <div class="speaker-role">Assistant Professor, Bioengineering</div>
    <div class="speaker-desc">at the Ostrander Polytechnic<br>Academy; Founding Member<br>of the Brackenfield Foundation</div>
  </div>
  <div class="abs speaker" style="left:651px;top:748px">
    <div class="speaker-name">Iris Menado, Ph.D.</div>
    <div class="speaker-role">Professor, Kessler University</div>
    <div class="speaker-desc">at the Ostrander Polytechnic<br>Academy; Founding Member<br>of the Brackenfield Foundation</div>
  </div>

  <div class="abs speaker" style="left:212px;top:900px">
    <div class="speaker-name">Felix Harlan, Ph.D.</div>
    <div class="speaker-role">Professor of Cellular</div>
    <div class="speaker-desc">at the Ostrander Polytechnic<br>Academy; Founding Member<br>of the Brackenfield Foundation</div>
  </div>
  <div class="abs speaker" style="left:347px;top:900px">
    <div class="speaker-name">Noel Strand, Ph.D.</div>
    <div class="speaker-role">Associate Professor of Pediatrics</div>
    <div class="speaker-desc">at the Ostrander Polytechnic<br>Academy; Founding Member<br>of the Brackenfield Foundation</div>
  </div>
  <div class="abs speaker" style="left:499px;top:900px">
    <div class="speaker-name">June Pascoe, Ph.D.</div>
    <div class="speaker-role">Professor, Department of Genetics</div>
    <div class="speaker-desc">at the Ostrander Polytechnic<br>Academy; Founding Member<br>of the Brackenfield Foundation</div>
  </div>
  <div class="abs speaker" style="left:651px;top:900px">
    <div class="speaker-name">Rami Ostrow, Ph.D.</div>
    <div class="speaker-role">Professor of Biology</div>
    <div class="speaker-desc">at the Ostrander Polytechnic<br>Academy; Founding Member<br>of the Brackenfield Foundation</div>
  </div>

  <footer class="abs footer">
    <p class="footer-text">
      Register and upload abstracts for the symposium at<br>
      <b>https://generegulation.valdmere-med.example</b><br>
      Registration and abstract submission closes on<br>
      <b>January 4, 2019</b>
    </p>
    <div class="partners">
      <div class="thanks">Thank you<br>to our Sponsor:</div>
      <div class="partner" style="left:68px;top:9px;font-size:12px"><i></i>Helixora Reagents</div>
      <div class="partner" style="left:6px;top:46px;width:108px"><i></i>Gene Regulation Centre</div>
      <div class="partner" style="left:124px;top:46px;width:112px"><i></i>Harrowgate School of Medicine</div>
    </div>
  </footer>
</main>
</body>
</html>
```